I need a business card design for a new company that will be doing consulting work around issues of cultural competency, and diversity and inclusion. I would like the design to be crisp and clear with bold but conservative colors and incorporate shades of blue

Target Market(s)

Small businesses, schools, non-profits

Industry/Entity Type

Consulting

Font styles to use
Serif
Sans Serif

Colors
0c5ba6
6b449b
3276b5
0292cd

Requirements
Must have
• A Morrow Venture (name of company)
• Lemlem Tavish
• CEO
• lemlem@amorrowventure.com
• (215)483-2756

```html
<!DOCTYPE html>
<html lang="en">
<head>
<meta charset="utf-8">
<title>A Morrow Venture – Business Card</title>
<link rel="stylesheet" href="https://fonts.googleapis.com/css2?family=Lato:wght@400;700&display=swap">
<style>
  :root {
    --navy-blue: #0c5ba6;
    --royal-purple: #6b449b;
    --mid-blue: #3276b5;
    --sky-blue: #0292cd;
    --ink: #1a1a1a;
    --paper: #ffffff;
    --backdrop: #e6e8eb;
  }
  * { margin: 0; padding: 0; box-sizing: border-box; }
  html, body {
    width: 1200px;
    height: 900px;
    overflow: hidden;
    background: var(--backdrop);
    font-family: "Lato", Arial, sans-serif;
  }
  .business-card {
    position: absolute;
    left: 75px;
    top: 150px;
    width: 1050px;
    height: 600px;
    background: var(--paper);
    border-radius: 34px;
    overflow: hidden;
    box-shadow: 0 10px 30px rgba(0,0,0,0.15);
  }
  .company-band {
    position: absolute;
    left: 0;
    top: 255px;
    width: 475px;
    height: 80px;
    background: var(--navy-blue);
    color: var(--paper);
    font-size: 33px;
    font-weight: 400;
    letter-spacing: 0.5px;
    line-height: 80px;
    padding-left: 32px;
    text-transform: uppercase;
    white-space: nowrap;
  }
  .person {
    position: absolute;
    right: 62px;
    top: 262px;
    text-align: right;
  }
  .person-name {
    color: var(--royal-purple);
    font-size: 60px;
    font-weight: 700;
    line-height: 1;
    white-space: nowrap;
  }
  .person-title {
    color: var(--ink);
    font-size: 34px;
    font-weight: 400;
    line-height: 1.1;
    margin-right: 24px;
  }
  .contact-list {
    position: absolute;
    left: 340px;
    top: 392px;
    border-left: 2px solid var(--royal-purple);
    padding-left: 20px;
    list-style: none;
  }
  .contact-item {
    display: flex;
    align-items: center;
    height: 48px;
    font-size: 26px;
    color: var(--ink);
    white-space: nowrap;
  }
  .contact-icon {
    width: 26px;
    height: 26px;
    margin-right: 16px;
    flex: none;
  }
  .web-domain { color: var(--royal-purple); }
  .edge-stripe {
    position: absolute;
    left: 0;
    bottom: 0;
    width: 1050px;
    height: 22px;
  }
</style>
</head>
<body>
  <article class="business-card">
    <div class="company-band">A Morrow Venture</div>

    <div class="person">
      <div class="person-name">Lemlem Tavish</div>
      <div class="person-title">CEO</div>
    </div>

    <ul class="contact-list">
      <li class="contact-item">
        <svg class="contact-icon" viewBox="0 0 24 24" aria-hidden="true">
          <path fill="var(--royal-purple)" d="M6.6 10.8c1.4 2.8 3.8 5.1 6.6 6.6l2.2-2.2c.3-.3.7-.4 1-.2 1.1.4 2.3.6 3.6.6.6 0 1 .4 1 1V20c0 .6-.4 1-1 1C10.6 21 3 13.4 3 4c0-.6.4-1 1-1h3.5c.6 0 1 .4 1 1 0 1.3.2 2.5.6 3.6.1.3 0 .7-.2 1z"/>
        </svg>
        <span>(215)483-2756</span>
      </li>
      <li class="contact-item">
        <svg class="contact-icon" viewBox="0 0 24 24" aria-hidden="true">
          <rect x="2" y="5" width="20" height="14" fill="var(--royal-purple)"/>
          <path d="M2 5l10 8 10-8M2 19l7.5-7M22 19l-7.5-7" fill="none" stroke="#fff" stroke-width="1.5"/>
        </svg>
        <span>lemlem@amorrowventure.com</span>
      </li>
      <li class="contact-item">
        <svg class="contact-icon" viewBox="0 0 24 24" aria-hidden="true">
          <circle cx="12" cy="12" r="10" fill="var(--royal-purple)"/>
          <g fill="none" stroke="#fff" stroke-width="1.2">
            <ellipse cx="12" cy="12" rx="4.5" ry="10"/>
            <path d="M2 12h20M4 7h16M4 17h16M12 2v20"/>
          </g>
        </svg>
        <span>www.<span class="web-domain">lemlemmorrowventure</span>.com</span>
      </li>
    </ul>

    <svg class="edge-stripe" viewBox="0 0 1050 22" preserveAspectRatio="none" aria-hidden="true">
      <polygon points="0,0 318,0 340,22 0,22" fill="var(--navy-blue)"/>
      <polygon points="328,0 1050,0 1050,22 350,22" fill="var(--sky-blue)"/>
    </svg>
  </article>
</body>
</html>
```